Label design for Japanese sake bottle (American market targeted)

We are launching a new sake product and the product concept is as below.

1. It is a draft which means it has a fresh taste
2. We want to emphasize on its cleanness and that it's easy drinkable
3. It is most likely to have a light blue transparent 300ml bottle
4. Product name is "Brisk Harbor Pour" although you don't have to make them stand out on the label. We are targeting non-Japanese customers, so all we want them to know is that "it is a sake and easy drinkable"
5. It is affordable. Its retail price per bottle would be somewhere around $10

Target Market(s)

Non-Japanese, preferably non-Asian liquor / grocery stores and restaurants

Industry/Entity Type

Glass Bottle

Font styles to use
Serif
Sans Serif
Decorative

Colors

Designer to choose colors to be used in the design.

Requirements
Must have
• The word "sake"
• Pureness, cleanness
Nice to have
• Any ideas for entering non-Asian market will be welcome!
Should not have
• Please do NOT make it similar to our competitors (which I would attach a few images of)

```html
<!DOCTYPE html>
<html lang="en">
<head>
<meta charset="UTF-8">
<title>Brisk Harbor Pour Sake Label</title>
<link rel="stylesheet" href="https://fonts.googleapis.com/css2?family=Montserrat:wght@400;800&display=swap">
<style>
  :root {
    --canvas-bg: #ffffff;
    --label-bg: #ffffff;
    --band-blue: #aee6f8;
    --band-blue-light: #c3edfa;
    --line-blue: #8fd6f2;
    --emblem-blue: #d6f3fc;
    --ink: #111111;
    --ink-soft: #222222;
  }
  * { margin: 0; padding: 0; box-sizing: border-box; }
  html, body {
    width: 1200px;
    height: 1188px;
    overflow: hidden;
    background: var(--canvas-bg);
  }
  .canvas {
    position: relative;
    width: 1200px;
    height: 1188px;
  }
  .label {
    position: absolute;
    left: 50px;
    top: 114px;
    width: 1100px;
    height: 959px;
    background: var(--label-bg);
    border: 1.5px solid var(--line-blue);
    overflow: hidden;
  }
  .label__band {
    position: absolute;
    left: 0;
    top: 0;
    width: 100%;
    height: 276px;
    background: linear-gradient(180deg, var(--band-blue-light), var(--band-blue));
  }
  .label__emblem {
    position: absolute;
    left: 372px;
    top: 100px;
    width: 356px;
    height: 387px;
  }
  .label__subtitle {
    position: absolute;
    left: 0;
    width: 100%;
    top: 512px;
    text-align: center;
    font-family: "Montserrat", sans-serif;
    font-weight: 400;
    font-size: 42px;
    letter-spacing: 0.5px;
    color: var(--ink-soft);
  }
  .label__title {
    position: absolute;
    left: 0;
    width: 100%;
    top: 568px;
    text-align: center;
    font-family: "Montserrat", sans-serif;
    font-weight: 800;
    font-size: 92px;
    line-height: 1;
    letter-spacing: 2px;
    color: var(--ink);
  }
  .label__volume {
    position: absolute;
    left: 0;
    width: 100%;
    top: 858px;
    text-align: center;
    font-family: "Montserrat", sans-serif;
    font-weight: 400;
    font-size: 33px;
    color: var(--ink-soft);
  }
</style>
</head>
<body>
  <main class="canvas">
    <section class="label">
      <div class="label__band" role="img" aria-label="Light blue woven texture band"></div>
      <svg class="label__emblem" viewBox="0 0 356 387" role="img" aria-label="Hexagonal line-art emblem of a sun over mountains and rolling fields">
        <path d="M178 4 L340 96 Q352 103 352 117 L352 270 Q352 284 340 291 L178 383 L16 291 Q4 284 4 270 L4 117 Q4 103 16 96 Z"
              fill="var(--emblem-blue)" stroke="var(--line-blue)" stroke-width="4"/>
      </svg>
      <p class="label__subtitle">Brisk Harbor Pour</p>
      <h1 class="label__title">SAKE</h1>
      <p class="label__volume">300ml</p>
    </section>
  </main>
</body>
</html>
```